I'm building an agency for marketing solutions but also medical education and patients education for pharmaceutical companies, medical societies and patient advocacy groups. We want to be perceived as the most innovative in the market. We work through design thinking solutions for campaigns and services.
I love some websites based on Swiss style design like www.quorlix.example
We are a small group of designers, physicians and creatives working together to deliver the best experiences in our market.
We decided to also use pixel forum expecting that we maybe found a great idea we didn't thought about yet.
Updates

I'm extending it for more 2 weeks

Reason: I need the best design you can. Only PSD. No code needed. Love Swiss style, like lumen 6 and quorlix.example I'm extending the deadline until get something great. Willing to extend as much as needed.

Target Market(s)

Pharmaceutical companies, physicians, medical societies, patients advocacy groups

Industry/Entity Type

Pharmaceutical

Font styles to use
Other font styles liked:
• Helvetia family

Colors

Designer to choose colors to be used in the design.

Requirements
Must have
• Must be innovative like www.quorlix.example
Nice to have
• Cool menus
Should not have
• Not to appear too much Comercial. We like to be a boutique in this market. Craftsmen working with less clients at time but delivering precious stones.

```html
<!DOCTYPE html>
<html lang="en">
<head>
<meta charset="utf-8">
<title>Brelvant — Design for Modern Medicine</title>
<link rel="stylesheet" href="https://fonts.googleapis.com/css2?family=Roboto:wght@100;300;400&family=Lato:wght@400;700&display=swap">
<style>
  :root{
    --bg:#1a1a1a;
    --tile:#222222;
    --footer:#2a2a2a;
    --orange:#dc6a1e;
    --web-orange:#f07a1c;
    --navy:#1d2f5e;
    --sky:#2ea3dc;
    --white:#ffffff;
    --text:#c4c4c4;
    --muted:#9a9a9a;
    --hero-dim:#b4b4b4;
  }
  *{margin:0;padding:0;box-sizing:border-box}
  html,body{width:1200px;height:1000px;overflow:hidden;background:var(--bg)}
  body{position:relative;font-family:"Roboto",Helvetica,Arial,sans-serif;color:var(--text)}
  .menu-toggle{position:absolute;left:973px;top:40px;width:24px;height:16px}
  .tile{position:absolute;overflow:hidden}

  .brand{left:203px;top:110px;width:189px;height:188px;background:var(--orange);display:flex;align-items:center;justify-content:center}
  .brand-name{font-family:"Lato",Helvetica,Arial,sans-serif;font-weight:700;font-size:27px;color:var(--white);letter-spacing:-.3px;margin-top:-6px}

  .card{background:var(--tile);padding:17px 14px}
  .card h2{font-family:"Lato",Helvetica,Arial,sans-serif;font-weight:700;font-size:15px;line-height:19px;color:#e4e4e4;margin-bottom:10px}
  .card p{font-weight:300;font-size:13px;line-height:20px;color:var(--text);white-space:nowrap}
  .intro{left:203px;top:313px;width:189px;height:188px}
  .print{left:808px;top:245px;width:189px;height:256px;padding-top:16px}
  .print h2{font-size:13px;margin-bottom:22px}
  .referrals{left:405px;top:515px;width:189px;height:188px;padding-top:14px}

  .hero{left:405px;top:110px;width:390px;height:391px;background:linear-gradient(180deg,#2b2b2b 0%,#222 50%,#1a1a1a 100%)}
  .hero-text{position:absolute;left:22px;top:29px;font-weight:100;font-size:35px;line-height:39px;color:var(--hero-dim);letter-spacing:-.6px;white-space:nowrap}
  .hero-text strong{font-weight:300;color:var(--white)}
  .hero-cta{position:absolute;left:24px;top:313px;font-weight:300;font-size:14px;color:var(--white)}

  .work-a{left:808px;top:110px;width:189px;height:121px;background:linear-gradient(120deg,#f3f6f9 0%,#dfe7ee 45%,#b9cad8 100%)}
  .work-a .topline{position:absolute;left:0;top:0;width:100%;height:8px;background:#fafafa}
  .work-a .nav{position:absolute;left:36px;top:100px;width:10px;height:9px;background:var(--sky)}
  .work-a .baseline{position:absolute;left:0;bottom:0;width:100%;height:4px;background:var(--sky)}

  .work-b{left:203px;top:515px;width:189px;height:188px;background:linear-gradient(135deg,#8f8f8f 0%,#c9c9c6 30%,#e6e8e4 60%,#cfdbd6 100%)}

  .work-c{left:607px;top:515px;width:189px;height:188px;background:#f4f4f4}
  .web-top{position:absolute;left:0;top:0;width:100%;height:11px;background:#fff}
  .web-nav{position:absolute;left:0;top:11px;width:100%;height:12px;background:var(--navy)}
  .web-photo{position:absolute;left:5px;top:23px;width:179px;height:74px;background:linear-gradient(180deg,#7a8a6e 0%,#3f5d9a 45%,#2c4a8c 100%)}
  .web-tabs{position:absolute;left:5px;top:97px;width:179px;height:18px;display:flex;gap:2px}
  .web-tabs span{flex:1;background:var(--web-orange)}
  .web-band{position:absolute;left:6px;top:123px;width:177px;height:26px;background:var(--navy)}
  .web-lines{position:absolute;left:8px;top:160px;width:60px;height:28px;background:repeating-linear-gradient(180deg,#c9c9c9 0 2px,transparent 2px 5px)}
  .web-thumb{position:absolute;left:74px;top:166px;width:48px;height:22px;background:linear-gradient(135deg,#8ea2b8,#d7dde3)}

  .work-d{left:808px;top:515px;width:189px;height:188px;background:linear-gradient(135deg,#e41c1c 0%,#d51212 55%,#c40d0d 100%)}

  .map{left:203px;top:718px;width:403px;height:188px;background:linear-gradient(135deg,#363636 0%,#2d2d2d 60%,#303030 100%)}
  .map svg{position:absolute;left:0;top:0}

  .contact{left:606px;top:718px;width:391px;height:188px;background:var(--footer);padding:29px 0 0 38px}
  .contact ul{list-style:none}
  .contact li{display:flex;align-items:center;height:29px;font-weight:300;font-size:12px;color:#b8b8b8}
  .contact li svg{width:11px;height:11px;margin-right:15px;fill:#aaa}
  .social{display:flex;gap:14px;margin-top:28px;font-weight:400;font-size:10px;color:#aaa}
  .copyright{position:absolute;left:203px;top:947px;font-weight:300;font-size:10px;color:var(--muted)}
</style>
</head>
<body>
  <svg class="menu-toggle" viewBox="0 0 24 16" aria-label="Menu">
    <rect x="0" y="0" width="24" height="1.6" fill="#fff"/>
    <rect x="0" y="7" width="24" height="1.6" fill="#fff"/>
    <rect x="0" y="14" width="24" height="1.6" fill="#fff"/>
  </svg>

  <div class="tile brand"><span class="brand-name">brelvant</span></div>

  <section class="tile hero" role="img" aria-label="Dimmed photograph of a modern open-plan office with desks and chairs">
    <p class="hero-text">We are a small group of<br><strong>designers</strong>, <strong>physicians</strong><br>and <strong>creatives</strong> working<br>together to deliver the<br><strong>best experiences</strong> in our<br>market.</p>
    <span class="hero-cta">Get Started</span>
  </section>

  <div class="tile work-a">
    <span class="topline"></span>
    <div role="img" aria-label="Website project screenshot with doctors reviewing a tablet"></div>
    <span class="nav"></span>
    <span class="baseline"></span>
  </div>

  <article class="tile card intro">
    <h2>We Design for<br>Modern Medicine</h2>
    <p>Our design team specializes<br>in creating modern sites<br>developed to get current and<br>potential patients the<br>information they need.</p>
  </article>

  <article class="tile card print">
    <h2>Print &amp; advertising are key.</h2>
    <p>Our creative<br>development and<br>design teams focus<br>on producing<br>innovative print<br>materials and ad<br>campaigns to get<br>you noticed.</p>
  </article>

  <div class="tile work-b" role="img" aria-label="Printed brochure project showing a woman holding a phone"></div>

  <article class="tile card referrals">
    <h2>Struggling to earn more<br>referrals?</h2>
    <p>Our team can provide market<br>training to help your practice<br>maximize the number of high<br>quality referrals you receive.</p>
  </article>

  <div class="tile work-c">
    <span class="web-top"></span>
    <span class="web-nav"></span>
    <div class="web-photo" role="img" aria-label="Group photo of a medical institute's staff outdoors"></div>
    <div class="web-tabs"><span></span><span></span><span></span></div>
    <span class="web-band"></span>
    <span class="web-lines"></span>
    <div class="web-thumb" role="img" aria-label="Small photo of clinicians"></div>
  </div>

  <div class="tile work-d" role="img" aria-label="Red brand identity project for a healthcare service"></div>

  <div class="tile map" role="img" aria-label="Dark street map of the office location">
    <svg width="403" height="188" viewBox="0 0 403 188">
      <circle cx="20" cy="21" r="13" fill="#f2f2f2"/>
      <path d="M20 12l-3 3h6zM20 30l-3-3h6zM11 21l3-3v6zM29 21l-3-3v6z" fill="#555"/>
      <line x1="20" y1="52" x2="20" y2="161" stroke="#e6e6e6" stroke-width="2"/>
      <rect x="15" y="47" width="10" height="10" fill="#f2f2f2"/>
      <path d="M17 52h6M20 49v6" stroke="#444" stroke-width="1.4"/>
      <rect x="15" y="110" width="10" height="5" fill="#f2f2f2"/>
      <rect x="15" y="156" width="10" height="10" fill="#f2f2f2"/>
      <path d="M17 161h6" stroke="#444" stroke-width="1.4"/>
      <path d="M194 76c-3.3 0-6 2.6-6 5.9 0 4.4 6 10.1 6 10.1s6-5.7 6-10.1c0-3.3-2.7-5.9-6-5.9z" fill="#fff"/>
      <circle cx="194" cy="82" r="2" fill="#2f2f2f"/>
    </svg>
  </div>

  <footer class="tile contact">
    <ul>
      <li><svg viewBox="0 0 12 12"><rect x="0" y="2" width="12" height="8"/><path d="M0 2l6 4 6-4" stroke="#2a2a2a" stroke-width="1" fill="none"/></svg>hello@brelvant.example</li>
      <li><svg viewBox="0 0 12 12"><path d="M2 0h2.5l1 3-1.5 1.2c.7 1.6 2 2.9 3.6 3.6L8.8 6.3l3 1V10c0 1-1 2-2 2C4.5 12 0 7.5 0 2 0 1 1 0 2 0z"/></svg>+44 1632 960 418</li>
      <li><svg viewBox="0 0 12 12"><path d="M6 0l6 5.5h-1.7V12H7.5V8h-3v4H1.7V5.5H0z"/></svg>14 Marlow Row, Ashcombe, Kent, UK</li>
    </ul>
    <div class="social"><span>Pagebook</span><span>Chirper</span><span>Workline</span></div>
  </footer>

  <p class="copyright">©2014 Brelvant</p>
</body>
</html>
```